Web design for insurance consultant. Target clients are (re)insurers, insurtech firms and vendor...

Need a crisp, modern website which will talk briefly about the firm and its principal founder. And, details around services offered for 3 different target clients: (1) re/insurance companies, (2) insurtech and IoT firms, and (3) vendors such as claims adjusting firms and home inspection firms supporting insurers

Target Market(s)

C-suite leaders of insurance companies, reinsurance companies, insurtech firms looking to innovate property insurance, and vendors selling to these insurance companies. Focus is property insurance in coastal, catastrophe-exposed regions of the US.

Coding

Coded - Design and coding required

Number of Pages Required

5+ page

Other font styles liked:
• not sure of font wanted - classic, but modern

Colors
0792cd
00a990

Requirements
Must have
• First box should use the attached "light bulb storm" picture as background.
• one change overall - remove "Get a quote" button - we do not sell to consumers, it's strictly B2B.
• For the 3 segments, use the pictures below. I could not find one I liked for "TPAs/Vendors", so welcome your suggestions.
• Want quotes in the boxes of each of the 3 market segments.
• Button on each of the 3 market segments would lead to content (not yet finished) that will explain in more detail the services to be provided to them.
Should not have
• don't want google maps or others showing location of business (waste of space, in my opinion)

```html
<!DOCTYPE html>
<html lang="en">
<head>
<meta charset="utf-8">
<title>Calloway – Insurance Consulting</title>
<link href="https://fonts.googleapis.com/css2?family=Montserrat:wght@500;600;700&family=Open+Sans:ital,wght@0,400;0,600;0,700;1,400;1,600&display=swap" rel="stylesheet">
<style>
:root{
  --green:#6b9e0f;
  --green-band:#6f9f0d;
  --blue:#1aa9dc;
  --ink:#222831;
  --body:#4a4f57;
  --muted:#8a8f97;
  --panel:#f3f7fc;
  --white:#ffffff;
  --phone:#f6e7a6;
  --line:#dfe5ec;
}
*{box-sizing:border-box;margin:0;padding:0}
html,body{width:1200px;height:2643px;overflow:hidden;background:var(--white)}
body{font-family:"Open Sans",Arial,sans-serif;color:var(--body);position:relative}
.page{position:absolute;left:82px;top:35px;width:1027px}
section,footer{position:relative;width:1027px}
.abs{position:absolute}
h1,h2,h3,h4,.btn{font-family:"Montserrat",Arial,sans-serif}
.btn{display:inline-block;background:var(--blue);color:var(--white);font-size:11px;font-weight:600;letter-spacing:.6px;text-transform:uppercase;text-align:center;border-radius:2px}

/* hero */
.hero{height:478px;background:var(--panel);overflow:hidden}
.brand{left:88px;top:44px;display:flex;align-items:center;gap:6px;font-family:"Montserrat",sans-serif;font-weight:700;font-size:15px;color:var(--green)}
.brand-dot{width:14px;height:14px;border-radius:50%;background:var(--blue)}
.social-top{right:88px;top:17px;display:flex;gap:18px}
.social-top span{width:8px;height:8px;border-radius:2px;background:#4d5866}
.nav{right:96px;top:47px;display:flex;gap:22px;font-family:"Montserrat",sans-serif;font-size:11px;font-weight:600;text-transform:uppercase;color:var(--green)}
.nav .active{color:var(--blue)}
.hero-art{left:290px;top:70px;width:620px;height:405px;border-radius:300px 300px 20px 20px;background:radial-gradient(ellipse at 60% 35%,#dfe3ea 0%,#e9eef5 45%,rgba(243,247,252,0) 75%)}
.hero-art-focus{left:600px;top:150px;width:280px;height:250px;border-radius:40px;background:linear-gradient(160deg,#7e8fe0 0%,#e8b2c4 55%,#f3f7fc 100%);opacity:.55}
.hero-title{left:88px;top:165px;font-size:38px;font-weight:700;line-height:46px;color:var(--green)}
.hero-title .blue{color:var(--blue)}
.hero-cta{left:88px;top:331px;width:128px;height:32px;line-height:32px;font-size:10px}

/* about */
.about{height:438px;background:var(--white)}
.about-frame{left:88px;top:62px;width:265px;height:234px;background:#e6edf7}
.about-frame-b{left:165px;top:215px;width:255px;height:85px;background:#e6edf7}
.about-photo{left:111px;top:86px;width:292px;height:186px;border:6px solid var(--white);background:linear-gradient(135deg,#f1f1f1 0%,#d9d9d9 55%,#6b6b6b 100%)}
.about-text{left:452px;top:95px;width:488px}
.about-text h2{font-size:26px;font-weight:700;color:var(--green)}
.about-text .role{font-family:"Open Sans",sans-serif;font-style:italic;font-weight:600;font-size:17px;color:#6a6f9a;margin:12px 0 16px}
.about-text p{font-size:12px;line-height:18px;margin-bottom:18px}

/* market */
.market{height:608px;background:var(--panel)}
.market h2{position:absolute;top:47px;width:100%;text-align:center;font-size:27px;font-weight:700;color:var(--green)}
.card{position:absolute;top:97px;width:252px;background:var(--white);border-radius:6px;box-shadow:0 3px 14px rgba(40,60,90,.10);text-align:center;padding:24px 18px 0}
.card-icon{width:40px;height:40px;border-radius:50%;margin:0 auto 14px;display:flex;align-items:center;justify-content:center}
.card h3{font-size:14px;font-weight:600;color:var(--ink);margin-bottom:14px}
.card .quote{font-size:10.5px;line-height:21px;text-align:left;color:#555}
.card .who{font-family:"Montserrat",sans-serif;font-size:13px;font-weight:600;color:var(--ink);line-height:16px;margin-top:2px}
.card .btn{width:176px;height:31px;line-height:31px;font-size:9.5px;margin:14px 0 26px}
.c1{left:97px}.c2{left:388px}.c3{left:678px}

/* contact band */
.band{height:176px;background:var(--green-band)}
.band h4{position:absolute;left:88px;top:34px;font-size:20px;font-weight:600;color:var(--white)}
.band .phone{position:absolute;left:88px;top:70px;font-family:"Montserrat",sans-serif;font-size:45px;font-weight:700;color:var(--phone)}
.band .outline{position:absolute;left:798px;top:72px;width:133px;height:33px;line-height:29px;border:2px solid var(--white);color:var(--white);font-family:"Montserrat",sans-serif;font-size:11px;font-weight:700;text-align:center}

/* testimonials */
.testimonials{height:306px;background:var(--white)}
.testimonials h2{position:absolute;top:46px;width:100%;text-align:center;font-size:27px;font-weight:700;color:var(--green)}
.avatar{left:242px;top:129px;width:76px;height:56px;border-radius:50%;background:#ffffff;border:3px solid #2d6aa0}
.t-body{left:342px;top:122px;width:440px}
.t-body h4{font-size:16px;font-weight:700;color:var(--ink)}
.t-body .title{font-size:10px;color:var(--muted);margin:3px 0 14px}
.t-body p{font-size:11.5px;font-style:italic;line-height:18px;color:#555}
.dots{left:485px;top:250px;display:flex;gap:8px}
.dots span{width:8px;height:8px;border-radius:50%;background:#d4d7db}
.dots .on{background:var(--blue)}

/* footer */
.footer{height:421px;background:var(--panel)}
.f-brand{left:88px;top:44px;font-family:"Montserrat",sans-serif;font-size:25px;font-weight:600;letter-spacing:3px;color:var(--green)}
.f-head{font-family:"Montserrat",sans-serif;font-size:11px;font-weight:700;color:var(--green);text-transform:uppercase}
.f-about{left:88px;top:96px;width:205px;font-size:10.5px;font-weight:600;line-height:19px;color:#3f444b}
.f-news{left:88px;top:241px}
.f-news-text{left:88px;top:280px;width:200px;font-size:10.5px;line-height:19px}
.subscribe{left:88px;top:328px;display:flex}
.subscribe .field{width:126px;height:27px;background:var(--white);border:1px solid var(--line)}
.subscribe .btn{width:70px;height:27px;line-height:27px;text-transform:none;font-family:"Open Sans",sans-serif;font-weight:400;font-size:11px;letter-spacing:0;border-radius:0}
.f-links{left:307px;top:46px}
.links{left:307px;top:86px;list-style:none;font-size:10.5px;line-height:29px}
.f-contact{left:307px;top:241px}
.contact-info{left:307px;top:280px;font-size:10.5px;line-height:18px}
.contact-info b{color:var(--ink)}
.f-social{left:307px;top:363px;display:flex;gap:7px}
.f-social span{width:27px;height:27px;border-radius:50%;background:var(--blue)}
.f-msg{left:526px;top:46px}
.form{left:526px;top:82px;width:413px}
.form .input{height:27px;background:var(--white);border:1px solid var(--line);margin-bottom:12px;font-size:10px;color:#8b9099;padding:6px 5px}
.form .area{height:101px}
.form .btn{display:block;margin:5px auto 0;width:117px;height:28px;line-height:28px;text-transform:none;font-family:"Open Sans",sans-serif;font-weight:400;letter-spacing:0;font-size:11px;border-radius:0}
.copyright{position:absolute;top:2453px;width:1200px;text-align:center;font-size:10.5px;color:#555}
.copyright b{color:var(--ink)}
</style>
</head>
<body>
<div class="page">

  <section class="hero">
    <div class="abs hero-art" role="img" aria-label="Illustration of a large umbrella sheltering family figures"></div>
    <div class="abs hero-art-focus" role="img" aria-label="Illustration of a family holding an insurance shield"></div>
    <div class="abs social-top"><span></span><span></span><span></span><span></span></div>
    <div class="abs brand"><span class="brand-dot"></span>calloway</div>
    <nav class="abs nav"><span class="active">Home</span><span>About me</span><span>Services</span><span>Contact us</span></nav>
    <h1 class="abs hero-title">Calloway provides<br>Complete<br><span class="blue">Insurence</span>Solutions</h1>
    <a class="abs btn hero-cta">Get started</a>
  </section>

  <section class="about">
    <div class="abs about-frame"></div>
    <div class="abs about-frame-b"></div>
    <div class="abs about-photo" role="img" aria-label="Illustration of the founder working at a laptop"></div>
    <div class="abs about-text">
      <h2>About Calloway Consulting</h2>
      <div class="role">Your Name</div>
      <p>Lorem ipsum dolor sit amet, consectetur adipiscing elit, sed do eiusmod tempor incididunt ut labore et dolore magna aliqua.</p>
      <p>Aut dolor id. Sint aliquam consequatur ex ex labore. Et quis dui dolor nulla dolores neque. Aspernatur consectetur omnis numquam quaerat. Sed fugiat nisi. Officiis veniam molestiae. Et vel ut quidem alias veritatis repudiandae ut fugit. Est ut eligendi aspernatur nulla voluptates veniam iusto vel quisquam. Fugit ut maxime incidunt accusantium totam repellendus eum error. Et repudiandae eum iste qui et ut ab alias.</p>
    </div>
  </section>

  <section class="market">
    <h2>Market areas</h2>
    <div class="card c1">
      <div class="card-icon" style="background:#fde4ec">
        <svg width="20" height="20" viewBox="0 0 20 20"><circle cx="10" cy="10" r="8" fill="none" stroke="#e5537f" stroke-width="1.4"/><path d="M5 11l3-3 3 4 4-4" fill="none" stroke="#e5537f" stroke-width="1.4"/></svg>
      </div>
      <h3>(Re)Insurers</h3>
      <p class="quote">"Calloway has a unique skill set in property cat that helped us refine our approach, particularly in the challenging Florida market. He was instrumental to us in distilling down our business plan, interactions and approvals with the Florida OIR, pricing and product development, and executing on our business plan."</p>
      <div class="who">Founder and President, Insurance Company</div>
      <a class="btn">Expand to services</a>
    </div>
    <div class="card c2">
      <div class="card-icon" style="background:#fdebd3">
        <svg width="18" height="18" viewBox="0 0 18 18"><rect x="2" y="2" width="14" height="14" fill="none" stroke="#e49a3c" stroke-width="1.4"/><path d="M2 7h14M8 7v9" stroke="#e49a3c" stroke-width="1.4"/></svg>
      </div>
      <h3>Insurtech / IoT</h3>
      <p class="quote">"We didn't realize how hard insurance is. Sam's operational insights and suggestions across the organization (i.e., from submission/bind through to claims handling) accelerated our launch and build-out by a number of months. He was especially valuable in helping us work through operationalizing new technologies to make the process smoother, more efficient, and consumer-friendly. "</p>
      <div class="who">Founder and COO, Insurtech MGA</div>
      <a class="btn">Expand to services</a>
    </div>
    <div class="card c3">
      <div class="card-icon" style="background:#dff8f4;margin-bottom:18px"></div>
      <h3>Vendors and TPAs</h3>
      <p class="quote">"Calloway knows everybody in this space. As important as his connections were to us, he also provided huge value to us in preparing and responding to RFPs. He's expensive, but worth every penny!"</p>
      <div class="who">CEO, Third Party Administrator</div>
      <a class="btn">Expand to services</a>
    </div>
  </section>

  <section class="band">
    <h4>Call For Quick Contact</h4>
    <div class="phone">+00 123456789</div>
    <a class="outline">CONTACT Us</a>
  </section>

  <section class="testimonials">
    <h2>Testimonials</h2>
    <div class="abs avatar"></div>
    <div class="abs t-body">
      <h4>Mr DUDE 1</h4>
      <div class="title">Ceo &amp; Founder</div>
      <p>Lorem ipsum dolor sit amet, consectetur adipiscing elit, sed do eiusmod tempor incididunt ut labore et dolore magna aliqua. Ut enim ad minim veniam, quis nostrud exercitation ullamco laboris nisi ut aliquip ex ea commodo consequat.</p>
    </div>
    <div class="abs dots"><span class="on"></span><span></span><span></span><span></span></div>
  </section>

  <footer class="footer">
    <div class="abs f-brand">CALLOWAY</div>
    <p class="abs f-about">Lorem ipsum dolor sit amet, consectetur adipiscing elit, sed do eiusmod tempor incididunt ut labore et dolore magna aliqua. Ut enim ad minim veniam, quis nostrud exercitation ullamco laboris nisi ut aliquip ex ea commodo consequat.</p>
    <div class="abs f-head f-news">Our Newsletter</div>
    <p class="abs f-news-text">Enter your mail id to get a part of our newsletter program</p>
    <div class="abs subscribe"><span class="field"></span><span class="btn">Subscribe</span></div>

    <div class="abs f-head f-links">Useful Links</div>
    <ul class="abs links"><li>Home</li><li>About Me</li><li>Services</li><li>Terms of service</li><li>Privacy policy</li></ul>
    <div class="abs f-head f-contact">Contact Us</div>
    <p class="abs contact-info">Building, Street name<br>district, State, Country<br><b>Phone:</b> +0 123456789<br><b>Email:</b>mail@calloway.com</p>
    <div class="abs f-social"><span></span><span></span><span></span><span></span></div>

    <div class="abs f-head f-msg">Send Us A Message</div>
    <div class="abs form">
      <div class="input">Your Name</div>
      <div class="input">Your Email</div>
      <div class="input">Subject</div>
      <div class="input area">Message</div>
      <span class="btn">Send Message</span>
    </div>
  </footer>
</div>
<div class="copyright">© Copyright <b>Calloway</b>. All Rights Reserved</div>
</body>
</html>
```